Morvex Business Card (intended for Business Card sized magnet)

Hi guys,

I would like to get a design for my business card for the restaurant. The design must be single sided as I intend to produce business card sized magnets.

The File attached must me on and I'm open for new ides

Can you please ensure that the design meets Cardowell's magnetic business card size specifications:

http://www.cardowell.example.au/custom-magnets.aspx?txi=15695&xnid=TopNav_Magnetic+Business+Cards+(linked+item)_Magnets_Marketing+Products&xnav=TopNav

Full Bleed Size (starting document size):
90 x 52 mm
1062 x 615 pixels
* Finished artwork should use the full bleed dimensions for best results.

Document Trim Size (final size after being cut):
87 x 49 mm
1028 x 579 pixels
* Please be sure to keep all text within the safe margin.

Resolution:
300 DPI

The winning design/source files need to meet these specifications.

Thanks
Updates

Hi guys, can I see more options please Thanks

```html
<!DOCTYPE html>
<html lang="en">
<head>
<meta charset="utf-8">
<title>Morvex – Business Card</title>
<link rel="stylesheet" href="https://fonts.googleapis.com/css2?family=Noto+Serif:wght@400&family=Roboto+Condensed:wght@300;400&display=swap">
<style>
  :root {
    --ink: #000000;
    --paper: #ffffff;
    --smoke: #3b3b3b;
    --tone-red: #c8102e;
    --tone-blue: #1ba3c8;
    --tone-yellow: #f8c500;
    --link-red: #d3132c;
  }
  html, body {
    margin: 0;
    padding: 0;
    width: 677px;
    height: 1200px;
    overflow: hidden;
    background: var(--ink);
  }
  .card {
    position: relative;
    width: 677px;
    height: 1200px;
    overflow: hidden;
    background:
      radial-gradient(ellipse 420px 360px at 50% 640px, var(--smoke) 0%, #1c1c1c 55%, var(--ink) 100%);
    color: var(--paper);
  }
  .brand-name {
    position: absolute;
    top: 66px;
    left: 0;
    width: 100%;
    margin: 0;
    text-align: center;
    font-family: "Noto Serif", serif;
    font-weight: 400;
    font-size: 168px;
    line-height: 1;
    color: var(--paper);
  }
  .rule {
    position: absolute;
    left: 22px;
    width: 633px;
    height: 6px;
    background: var(--paper);
  }
  .rule--top { top: 259px; }
  .rule--bottom { top: 466px; }
  .ornament-band {
    position: absolute;
    left: 22px;
    top: 275px;
    width: 633px;
    height: 182px;
    background: linear-gradient(180deg, #8c8c8c 0%, #6e6e6e 100%);
  }
  .awning-art {
    position: absolute;
    left: 22px;
    top: 506px;
    width: 633px;
    height: 208px;
    background: linear-gradient(90deg, var(--tone-red) 0%, var(--tone-blue) 50%, var(--tone-yellow) 100%);
  }
  .contact-line {
    position: absolute;
    left: 0;
    width: 100%;
    margin: 0;
    text-align: center;
    font-family: "Roboto Condensed", sans-serif;
    font-weight: 300;
    line-height: 1;
    color: var(--paper);
    transform: translateY(-50%);
  }
  .contact-line--street { top: 826px; font-size: 37px; }
  .contact-line--suburb { top: 874px; font-size: 37px; }
  .contact-line--phone { top: 936px; font-size: 60px; }
  .contact-line--email { top: 996px; font-size: 38px; }
  .contact-line--web {
    top: 1114px;
    font-size: 44px;
    font-weight: 400;
    color: var(--link-red);
  }
</style>
</head>
<body>
  <main class="card">
    <h1 class="brand-name">Morvex</h1>

    <div class="rule rule--top"></div>
    <div class="ornament-band" role="img" aria-label="Band of white interlaced eight-pointed star ornaments with red, blue and yellow centres"></div>
    <div class="rule rule--bottom"></div>

    <div class="awning-art" role="img" aria-label="Illustration of three rounded awnings in red, blue and yellow with a fork and spoon"></div>

    <p class="contact-line contact-line--street">412 Larkspur Rd</p>
    <p class="contact-line contact-line--suburb">Elmsford East, 3199</p>
    <p class="contact-line contact-line--phone">03 9000 4127</p>
    <p class="contact-line contact-line--email">Morvex412@mailbox.example</p>
    <p class="contact-line contact-line--web">www.morvex.example.au</p>
  </main>
</body>
</html>
```